Looking for a clean, modern, and professional business card design that reflects Valtrin Systems

The design should include the company logo, contact details, and align with our brand identity. Please use a sophisticated and minimalist style, incorporating [specific colors, if applicable]. Creativity is welcome, but the card must maintain a polished and professional appearance.

Details to Include:

Name: Lou Marchetti
Title: VP Sales / Operations
Company: Valtrin Systems
Phone: 304.617.2285
Email: lou@valtrinsystems.example
Website: www.valtrinsystems.example

```html
<!DOCTYPE html>
<html lang="en">
<head>
<meta charset="utf-8">
<title>Valtrin Systems – Business Card</title>
<link rel="stylesheet" href="https://fonts.googleapis.com/css2?family=Questrial&display=swap">
<style>
  :root {
    --backdrop: #9d9d9d;
    --brand-blue: #1f5ea8;
    --brand-blue-deep: #174c8c;
    --accent-blue: #2f6fc0;
    --accent-light: #6a9fe0;
    --paper: #ffffff;
    --ink: #1c1c1c;
    --ink-soft: #333333;
  }
  * { box-sizing: border-box; margin: 0; padding: 0; }
  html, body { width: 900px; height: 1200px; overflow: hidden; }
  body {
    background: var(--backdrop);
    font-family: "Questrial", "Century Gothic", sans-serif;
    position: relative;
  }
  .card {
    position: absolute;
    left: 100px;
    width: 700px;
    height: 400px;
    border-radius: 26px;
    overflow: hidden;
  }

  /* Front */
  .card-front { top: 110px; background: var(--brand-blue); color: var(--paper); }
  .front-decor-left {
    position: absolute; left: 0; bottom: 0; width: 230px; height: 240px;
    background: radial-gradient(circle at 0% 100%, rgba(23,76,140,0.85), rgba(31,94,168,0) 70%);
  }
  .front-decor-right {
    position: absolute; right: 0; top: 0; width: 220px; height: 180px;
    background: radial-gradient(circle at 100% 0%, rgba(23,76,140,0.9), rgba(31,94,168,0) 70%);
  }
  .wordmark {
    position: absolute; left: 0; right: 0; top: 120px;
    display: flex; align-items: center; justify-content: center; gap: 16px;
    font-size: 46px; letter-spacing: 2px; color: var(--paper);
  }
  .wordmark-dot { width: 16px; height: 16px; border-radius: 50%; background: var(--paper); }
  .front-rule { position: absolute; height: 2px; background: var(--paper); }
  .front-rule.upper { left: 330px; right: 40px; top: 225px; }
  .front-rule.lower { left: 40px; right: 330px; top: 350px; }
  .front-url {
    position: absolute; right: 40px; top: 245px;
    font-size: 17px; letter-spacing: 0.3px;
  }

  /* Back */
  .card-back { top: 690px; background: var(--paper); color: var(--ink); }
  .back-decor {
    position: absolute; right: 0; top: 0; width: 300px; height: 250px;
    background: linear-gradient(135deg, rgba(255,255,255,0) 20%, var(--accent-light) 45%, var(--brand-blue) 75%, var(--brand-blue-deep));
    clip-path: polygon(15% 0, 100% 0, 100% 100%, 75% 100%);
  }
  .holder { position: absolute; left: 56px; top: 90px; }
  .holder-name {
    font-size: 34px; color: var(--brand-blue); text-transform: uppercase; letter-spacing: 0.5px;
  }
  .holder-title { font-size: 30px; color: var(--ink); margin-top: 2px; }
  .back-rule { position: absolute; height: 2px; background: var(--brand-blue); }
  .back-rule.upper { left: 300px; right: 120px; top: 225px; }
  .back-rule.lower { left: 56px; right: 260px; top: 360px; }
  .contact { position: absolute; left: 56px; top: 245px; font-size: 17px; color: var(--ink-soft); }
  .contact-company { font-size: 17px; color: var(--ink); margin-bottom: 8px; font-weight: 400; }
  .contact-list { list-style: none; }
  .contact-list li { display: flex; align-items: center; gap: 12px; height: 24px; }
  .contact-list svg { width: 18px; height: 18px; flex: none; }
</style>
</head>
<body>

  <section class="card card-front" aria-label="Card front">
    <div class="front-decor-left" role="img" aria-label="Faint geometric bar and dot pattern"></div>
    <div class="front-decor-right" role="img" aria-label="Faint geometric bar and dot pattern"></div>
    <div class="wordmark"><span class="wordmark-dot"></span><span>Valtrin Systems</span></div>
    <div class="front-rule upper"></div>
    <p class="front-url">www.valtrinsystems.example</p>
    <div class="front-rule lower"></div>
  </section>

  <section class="card card-back" aria-label="Card back">
    <div class="back-decor" role="img" aria-label="Blue geometric bar and dot pattern in the corner"></div>
    <div class="holder">
      <h1 class="holder-name">Lou Marchetti</h1>
      <p class="holder-title">VP Sales / Operations</p>
    </div>
    <div class="back-rule upper"></div>
    <div class="contact">
      <p class="contact-company">Valtrin Systems</p>
      <ul class="contact-list">
        <li>
          <svg viewBox="0 0 20 20" aria-hidden="true"><circle cx="10" cy="10" r="9" fill="var(--brand-blue)"/><path d="M7 5.5c-.8.4-1.2 1.2-.9 2.3.8 2.7 2.6 4.5 5.2 5.3 1 .3 1.9-.1 2.3-.9l-1.6-1.5-1.1.6c-1-.5-1.8-1.3-2.2-2.3l.6-1.1z" fill="#fff"/></svg>
          <span>304.617.2285</span>
        </li>
        <li>
          <svg viewBox="0 0 20 20" aria-hidden="true"><rect x="2" y="4.5" width="16" height="11" fill="none" stroke="var(--brand-blue)" stroke-width="1.5"/><path d="M2 4.5l8 6 8-6" fill="none" stroke="var(--brand-blue)" stroke-width="1.5"/></svg>
          <span>lou@valtrinsystems.example</span>
        </li>
        <li>
          <svg viewBox="0 0 20 20" aria-hidden="true"><circle cx="10" cy="10" r="9" fill="var(--brand-blue)"/><g fill="none" stroke="#fff" stroke-width="1"><ellipse cx="10" cy="10" rx="3.5" ry="8"/><path d="M2 10h16M3.5 6h13M3.5 14h13"/></g></svg>
          <span>www.valtrinsystems.example</span>
        </li>
      </ul>
    </div>
    <div class="back-rule lower"></div>
  </section>

</body>
</html>
```